Faris Methani Business Card

I would like an elegant business card design in both english and arabic.

Ideally a logo design with my name in Arabic (could be a tiger for example)

It should have my Name : Faris Methani
Title: Advisor / Investor
Tel. UAE +971 558 274 903
UK +44 7821 560 287
Email. farmethani412@mailvane.net

I am an active angle investor and have many business interests in the TMT space and invest globally, the design needs to be fresh, elegant and striking.

The design should be catching and grab one's attention when they view the card.

Front card should be in English and Reverse in Arabic....

Target Market(s)

Global Investors, CEO's

Industry/Entity Type

Business

Contact Information for Business Card

Title: Advisor / Investor
Tel. UAE +971 558 274 903
UK +44 7821 560 287

Font styles to use
Serif
Other font styles liked:
• Palantino

Requirements
Must have
• A striking design with a play of my name in Arabic, could be my name that is designed as a tiger for example

```html
<!DOCTYPE html>
<html lang="en">
<head>
<meta charset="utf-8">
<title>Faris Methani – Business Card</title>
<link rel="stylesheet" href="https://fonts.googleapis.com/css2?family=Libre+Baskerville:wght@400;700&family=Amiri:wght@400;700&display=swap">
<style>
  :root {
    --page: #2b2a2a;
    --paper: #ffffff;
    --ink: #2f2f2f;
    --accent: #f3952f;
    --accent-faint: #fbe3c8;
    --fold: rgba(0,0,0,0.10);
  }
  * { margin: 0; padding: 0; box-sizing: border-box; }
  html, body { width: 1200px; height: 1200px; overflow: hidden; }
  body {
    background: var(--page);
    display: flex;
    flex-direction: column;
    align-items: center;
    justify-content: center;
    gap: 60px;
    font-family: "Libre Baskerville", "Palatino Linotype", Palatino, serif;
    color: var(--ink);
  }
  .card {
    position: relative;
    width: 900px;
    height: 500px;
    background: var(--paper);
    overflow: hidden;
    box-shadow: 0 12px 30px rgba(0,0,0,0.35);
  }
  .edge-bar {
    position: absolute;
    width: 18px;
    background: var(--accent);
  }
  .edge-bar--left { left: 0; }
  .edge-bar--right { right: 0; }
  .card--back .edge-bar--left { top: 190px; bottom: 40px; }
  .card--back .edge-bar--right { top: 40px; height: 220px; }
  .card--front .edge-bar--left { top: 40px; height: 240px; }
  .card--front .edge-bar--right { top: 220px; bottom: 40px; }

  .faint-mark {
    position: absolute;
    right: -120px;
    top: -60px;
    width: 560px;
    height: 560px;
    border-radius: 50%;
    border: 70px solid var(--accent-faint);
    opacity: 0.7;
  }
  .contact-panel {
    position: absolute;
    left: 380px;
    top: 0;
    right: 0;
    bottom: 0;
    background: linear-gradient(90deg, var(--fold) 0, rgba(0,0,0,0) 26px);
  }
  .identity {
    position: absolute;
    left: 40px;
    width: 340px;
    top: 0;
    bottom: 0;
    display: flex;
    flex-direction: column;
    align-items: center;
    justify-content: center;
    text-align: center;
  }
  .brand-dot {
    width: 96px;
    height: 96px;
    border-radius: 50%;
    background: var(--accent);
    margin-bottom: 26px;
  }
  .name-en {
    font-size: 34px;
    font-weight: 700;
    letter-spacing: 1px;
    text-transform: uppercase;
    line-height: 1.1;
  }
  .title-en {
    font-size: 22px;
    font-weight: 700;
    color: var(--accent);
    margin-top: 6px;
  }
  .name-ar, .title-ar {
    font-family: "Amiri", serif;
    direction: rtl;
  }
  .name-ar { font-size: 56px; font-weight: 700; line-height: 1.1; }
  .title-ar { font-size: 28px; font-weight: 700; color: var(--accent); }

  .contacts {
    position: absolute;
    left: 440px;
    top: 150px;
    font-size: 22px;
    line-height: 1.45;
  }
  .contact-row { display: flex; align-items: flex-start; gap: 14px; }
  .contact-row + .contact-row { margin-top: 34px; }
  .contact-icon { width: 22px; height: 22px; flex: none; margin-top: 6px; }
  .digits-ar { font-family: "Amiri", serif; font-size: 26px; line-height: 1.25; }
</style>
</head>
<body>

  <section class="card card--back" lang="ar">
    <div class="faint-mark" aria-hidden="true"></div>
    <div class="contact-panel" aria-hidden="true"></div>
    <div class="edge-bar edge-bar--left"></div>
    <div class="edge-bar edge-bar--right"></div>
    <div class="identity">
      <div class="brand-dot" aria-hidden="true"></div>
      <h2 class="name-ar">فارس ميثاني</h2>
      <p class="title-ar">مستشار / مستثمر</p>
    </div>
    <div class="contacts" dir="ltr">
      <div class="contact-row">
        <svg class="contact-icon" viewBox="0 0 24 24"><path fill="#f3952f" d="M2 9c0-3 4-5 10-5s10 2 10 5v2h-5V9H7v2H2zM6 12h12l3 8H3z"/><circle cx="12" cy="16" r="2" fill="#fff"/></svg>
        <div class="digits-ar">UAE +٩٧١ ٥٥٨ ٢٧٤ ٩٠٣<br>UK +٤٤ ٧٨٢١ ٥٦٠ ٢٨٧</div>
      </div>
      <div class="contact-row">
        <svg class="contact-icon" viewBox="0 0 24 24"><rect x="2" y="5" width="20" height="14" fill="#f3952f"/><path d="M2 5l10 8 10-8" fill="none" stroke="#fff" stroke-width="1.6"/></svg>
        <div>farmethani412@mailvane.net</div>
      </div>
    </div>
  </section>

  <section class="card card--front">
    <div class="faint-mark" aria-hidden="true"></div>
    <div class="contact-panel" aria-hidden="true"></div>
    <div class="edge-bar edge-bar--left"></div>
    <div class="edge-bar edge-bar--right"></div>
    <div class="identity">
      <div class="brand-dot" aria-hidden="true"></div>
      <h1 class="name-en">Faris Methani</h1>
      <p class="title-en">Advisor / Investor</p>
    </div>
    <div class="contacts">
      <div class="contact-row">
        <svg class="contact-icon" viewBox="0 0 24 24"><path fill="#f3952f" d="M2 9c0-3 4-5 10-5s10 2 10 5v2h-5V9H7v2H2zM6 12h12l3 8H3z"/><circle cx="12" cy="16" r="2" fill="#fff"/></svg>
        <div>UAE +971 558 274 903<br>UK +44 7821 560 287</div>
      </div>
      <div class="contact-row">
        <svg class="contact-icon" viewBox="0 0 24 24"><rect x="2" y="5" width="20" height="14" fill="#f3952f"/><path d="M2 5l10 8 10-8" fill="none" stroke="#fff" stroke-width="1.6"/></svg>
        <div>farmethani412@mailvane.net</div>
      </div>
    </div>
  </section>

</body>
</html>
```